Need DL Flyer for Real Estate Drops

We need a real estate flyer ,double sided. With content on 1 side like: Want to know what's your house is worth " contact us today and on other side agent details. We are looking for an ongoing partnership with designer so this assignment will be ongoing

```html
<!DOCTYPE html>
<html lang="en">
<head>
<meta charset="utf-8">
<title>Kestra Real Estate – DL Flyer</title>
<link rel="stylesheet" href="https://fonts.googleapis.com/css2?family=Montserrat:wght@300;500;600;700;800;900&display=swap">
<style>
  :root{
    --red:#c62729;
    --navy:#0f1a52;
    --white:#ffffff;
    --paper:#f4f4f6;
    --sky-top:#0a6fd8;
    --sky-low:#7fc0f0;
    --house:#d9dde2;
    --ring:#e9a9aa;
    --bg-light:#d0cfd0;
    --bg-dark:#8c8c8c;
  }
  *{margin:0;padding:0;box-sizing:border-box}
  html,body{width:1200px;height:1200px;overflow:hidden}
  body{
    background:linear-gradient(135deg,var(--bg-light) 0%,#b5b4b5 55%,var(--bg-dark) 100%);
    font-family:'Montserrat',sans-serif;
    position:relative;
  }
  .flyer{position:absolute;top:175px;width:426px;height:850px;overflow:hidden}
  .flyer--front{left:145px}
  .flyer--back{left:629px}
  .flyer__bg{position:absolute;inset:0}
  .abs{position:absolute}

  .brand{position:absolute;top:50px;left:0;width:100%;display:flex;justify-content:center;align-items:center;gap:12px}
  .brand__mark{width:34px;height:34px}
  .brand__name{font-weight:700;font-size:27px;color:var(--white);letter-spacing:.2px}

  /* front */
  .front-head{position:absolute;left:0;width:100%;text-align:center;color:var(--white)}
  .front-head--bold{top:125px;font-weight:800;font-size:34px}
  .front-head--light{top:165px;font-weight:300;font-size:34px}
  .worth-pill{position:absolute;left:62px;top:213px;width:301px;height:46px;border-radius:23px;background:var(--navy)}
  .worth-pill__lead{position:absolute;left:16px;top:0;line-height:46px;font-weight:800;font-size:30px;color:var(--white)}
  .worth-pill__key{position:absolute;right:0;top:0;width:132px;height:46px;border-radius:23px;background:var(--white);color:var(--red);font-weight:800;font-size:30px;line-height:46px;text-align:center}
  .cta-label{position:absolute;left:0;top:704px;width:100%;text-align:center;color:var(--white);font-weight:700;font-size:19px}
  .phone-pill{position:absolute;left:66px;top:741px;width:315px;height:55px;border-radius:28px;background:var(--red);border:2px solid var(--white);color:var(--white);font-weight:800;font-size:33px;line-height:51px;padding-left:28px}
  .phone-badge{position:absolute;left:45px;top:747px;width:43px;height:43px;border-radius:50%;background:var(--navy);border:2px solid var(--white);display:flex;align-items:center;justify-content:center}
  .web-line{position:absolute;left:50px;top:806px;display:flex;align-items:center;gap:10px;color:var(--white);font-weight:700;font-size:17.5px}
  .web-line__icon{width:24px;height:24px}

  /* back */
  .back-head{position:absolute;left:0;width:100%;text-align:center;font-weight:800;color:var(--white)}
  .back-head--lead{top:121px;font-size:27px}
  .back-head--big{top:148px;font-size:56px;line-height:70px;font-weight:900}
  .back-head--big .hl{color:var(--red)}
  .back-head--tail{top:214px;font-size:35px}
  .agent-intro{position:absolute;left:0;width:100%;text-align:center;font-weight:700;font-size:26px}
  .agent-intro--navy{top:316px;color:var(--navy)}
  .agent-intro--red{top:346px;color:var(--red)}
  .card-photo{position:absolute;left:42px;top:448px;width:124px;height:124px;border-radius:50%;border:5px solid var(--ring);background:radial-gradient(circle at 50% 40%,#f4f6f8 0%,#c9d3e3 70%,#8ea3c6 100%)}
  .agent-name{position:absolute;left:188px;top:420px;color:var(--red);font-weight:800;font-size:23px}
  .agent-role{position:absolute;left:188px;top:448px;color:var(--white);font-weight:700;font-size:11.5px;line-height:16px}
  .agent-rule{position:absolute;left:188px;top:481px;width:196px;height:1px;background:var(--white)}
  .contact-row{position:absolute;left:185px;display:flex;align-items:flex-start;gap:8px;color:var(--white);font-weight:500;font-size:14.5px;line-height:19px}
  .contact-row__icon{width:15px;height:15px;margin-top:2px;flex:none}
  .social-dot{position:absolute;top:497px;width:24px;height:24px;border-radius:50%}
  .email-pill{position:absolute;left:79px;top:587px;width:313px;height:24px;border-radius:12px;background:var(--white);display:flex;align-items:center;justify-content:center;gap:8px;color:var(--navy);font-weight:500;font-size:14.5px}
  .email-pill .hl{color:var(--red);font-weight:700}
  .showcase{position:absolute;top:651px;width:118px;height:118px;border-radius:50%;border:2px solid var(--red);padding:4px;background:var(--white)}
  .showcase__fill{width:100%;height:100%;border-radius:50%}
  .web-band{position:absolute;left:38px;top:811px;display:flex;align-items:center;gap:10px;color:var(--white);font-weight:700;font-size:19px}
</style>
</head>
<body>

<!-- FRONT -->
<section class="flyer flyer--front">
  <svg class="flyer__bg" width="426" height="850" viewBox="0 0 426 850">
    <defs>
      <linearGradient id="skyFront" x1="0" y1="0" x2="0" y2="1">
        <stop offset="0" stop-color="var(--sky-top)"/>
        <stop offset=".5" stop-color="var(--sky-low)"/>
        <stop offset=".8" stop-color="var(--house)"/>
        <stop offset="1" stop-color="#8aa36a"/>
      </linearGradient>
    </defs>
    <rect width="426" height="850" fill="var(--red)"/>
    <rect y="540" width="426" height="310" fill="var(--navy)"/>
    <path d="M0,409 C60,320 130,286 202,286 L426,286 L426,546 C380,620 300,678 165,678 L0,678 Z" fill="url(#skyFront)" role="img" aria-label="Photo of a modern two-storey white house under a blue sky"/>
  </svg>

  <div class="brand">
    <svg class="brand__mark" viewBox="0 0 34 34"><rect width="34" height="34" rx="4" fill="var(--navy)"/></svg>
    <span class="brand__name">Kestra Real Estate</span>
  </div>

  <div class="front-head front-head--bold">Want to know</div>
  <div class="front-head front-head--light">What's your</div>
  <div class="worth-pill">
    <span class="worth-pill__lead">House is</span>
    <span class="worth-pill__key">worth</span>
  </div>

  <div class="cta-label">CONTACT US TODAY</div>
  <div class="phone-pill">(03) 9000 4127</div>
  <div class="phone-badge">
    <svg width="22" height="22" viewBox="0 0 24 24"><path fill="var(--white)" d="M6.6 10.8c1.4 2.8 3.8 5.1 6.6 6.6l2.2-2.2c.3-.3.7-.4 1-.2 1.1.4 2.3.6 3.6.6.6 0 1 .4 1 1V20c0 .6-.4 1-1 1C10.6 21 3 13.4 3 4c0-.6.4-1 1-1h3.5c.6 0 1 .4 1 1 0 1.3.2 2.5.6 3.6.1.3 0 .7-.2 1z"/></svg>
  </div>
  <div class="web-line">
    <svg class="web-line__icon" viewBox="0 0 24 24"><circle cx="12" cy="12" r="12" fill="var(--white)"/><g fill="none" stroke="var(--red)" stroke-width="1.3"><circle cx="12" cy="12" r="7"/><ellipse cx="12" cy="12" rx="3" ry="7"/><path d="M5 12h14M6 8.5h12M6 15.5h12"/></g></svg>
    <span>www.kestrarealestate.com.au</span>
  </div>
</section>

<!-- BACK -->
<section class="flyer flyer--back">
  <svg class="flyer__bg" width="426" height="850" viewBox="0 0 426 850">
    <defs>
      <clipPath id="cardClip"><rect x="17" y="407" width="392" height="221" rx="16"/></clipPath>
    </defs>
    <rect width="426" height="850" fill="var(--navy)"/>
    <path d="M0,409 C60,320 130,286 202,286 L426,286 L426,850 L0,850 Z" fill="var(--paper)"/>
    <path d="M0,799 L300,799 C385,799 420,780 426,745 L426,850 L0,850 Z" fill="var(--red)"/>
    <line x1="76" y1="388" x2="349" y2="388" stroke="var(--navy)" stroke-width="1.2" stroke-dasharray="2 3"/>
    <path d="M206,388 L220,388 L213,397 Z" fill="var(--red)"/>
    <ellipse cx="213" cy="636" rx="150" ry="6" fill="#000" opacity=".12"/>
    <g clip-path="url(#cardClip)">
      <rect x="17" y="407" width="392" height="221" fill="var(--navy)"/>
      <path d="M17,407 L157,407 C157,520 90,600 17,628 Z" fill="var(--red)"/>
    </g>
    <ellipse cx="81" cy="780" rx="45" ry="4" fill="#000" opacity=".1"/>
    <ellipse cx="209" cy="780" rx="45" ry="4" fill="#000" opacity=".1"/>
    <ellipse cx="337" cy="780" rx="45" ry="4" fill="#000" opacity=".1"/>
  </svg>

  <div class="brand">
    <svg class="brand__mark" viewBox="0 0 34 34"><rect width="34" height="34" rx="4" fill="var(--red)"/></svg>
    <span class="brand__name">Kestra Real Estate</span>
  </div>

  <div class="back-head back-head--lead">Do You Want to</div>
  <div class="back-head back-head--big"><span class="hl">Buy</span> or <span class="hl">Sell</span></div>
  <div class="back-head back-head--tail">Your House?</div>

  <div class="agent-intro agent-intro--navy">Contact Our</div>
  <div class="agent-intro agent-intro--red">Real Estate Agent</div>

  <div class="card-photo" role="img" aria-label="Portrait photo of the agent"></div>
  <div class="agent-name">Dev Amberley</div>
  <div class="agent-role">Managing Director / LEA,<br>Kestra Real Estate</div>
  <div class="agent-rule"></div>

  <div class="contact-row" style="top:493px">
    <svg class="contact-row__icon" viewBox="0 0 24 24"><circle cx="12" cy="12" r="12" fill="var(--red)"/><path transform="translate(5 5) scale(.58)" fill="var(--white)" d="M6.6 10.8c1.4 2.8 3.8 5.1 6.6 6.6l2.2-2.2c.3-.3.7-.4 1-.2 1.1.4 2.3.6 3.6.6.6 0 1 .4 1 1V20c0 .6-.4 1-1 1C10.6 21 3 13.4 3 4c0-.6.4-1 1-1h3.5c.6 0 1 .4 1 1 0 1.3.2 2.5.6 3.6.1.3 0 .7-.2 1z"/></svg>
    <span>03 9000 4127</span>
  </div>
  <div class="contact-row" style="top:515px">
    <svg class="contact-row__icon" viewBox="0 0 24 24"><circle cx="12" cy="12" r="12" fill="var(--red)"/><rect x="8.5" y="5.5" width="7" height="13" rx="1.5" fill="none" stroke="var(--white)" stroke-width="1.6"/></svg>
    <span>0400111278</span>
  </div>
  <div class="contact-row" style="top:539px">
    <svg class="contact-row__icon" viewBox="0 0 24 24"><circle cx="12" cy="12" r="12" fill="var(--red)"/><path transform="translate(5.5 5) scale(.55)" fill="var(--white)" d="M12 2a7 7 0 0 0-7 7c0 5 7 13 7 13s7-8 7-13a7 7 0 0 0-7-7zm0 9.5a2.5 2.5 0 1 1 0-5 2.5 2.5 0 0 1 0 5z"/></svg>
    <span>14/8 Harbourline Drive,<br>Larkfield 3095</span>
  </div>
  <div class="social-dot" style="left:326px;background:var(--white)"></div>
  <div class="social-dot" style="left:356px;background:var(--red);border:2px solid var(--white)"></div>

  <div class="email-pill">
    <svg width="13" height="10" viewBox="0 0 13 10"><rect width="13" height="10" fill="var(--red)"/><path d="M0,0 L6.5,5.5 L13,0" fill="none" stroke="var(--white)" stroke-width="1.2"/></svg>
    <span>dev@<span class="hl">kestrarealestate</span>.com.au</span>
  </div>

  <div class="showcase" style="left:22px"><div class="showcase__fill" role="img" aria-label="Photo of a new single-storey home under a cloudy sky" style="background:linear-gradient(#6f7680,#c9c7c2 60%,#8a7a66)"></div></div>
  <div class="showcase" style="left:150px"><div class="showcase__fill" role="img" aria-label="Photo of a lit family home at dusk" style="background:linear-gradient(#b9b2b8,#8a6a55 60%,#d8d8d6)"></div></div>
  <div class="showcase" style="left:278px"><div class="showcase__fill" role="img" aria-label="Photo of a bright white living room interior" style="background:linear-gradient(#f2f2f2,#dcdcdc 60%,#8d6e56)"></div></div>

  <div class="web-band">
    <svg class="web-line__icon" viewBox="0 0 24 24"><circle cx="12" cy="12" r="12" fill="var(--navy)"/><g fill="none" stroke="var(--white)" stroke-width="1.3"><circle cx="12" cy="12" r="7"/><ellipse cx="12" cy="12" rx="3" ry="7"/><path d="M5 12h14M6 8.5h12M6 15.5h12"/></g></svg>
    <span>www.kestrarealestate.com.au</span>
  </div>
</section>

</body>
</html>
```